E-liquid (Vape) company needs label design for re-brand

We are a e-liquid producer for the vaping industry and we are launching two new juices with a fresh logo and label. We also want to re-brand some of the older liquids with the new label. We already have a logo and a label design idea but need the labels to stand out from our competitors and communicate quality and sophistication, with just a little fun added to the mix.
We want to incorporate our old logo on the side or "back" of the label to reasure our existing fans that it is still the same quality they are used to.
Labels will be 88mm x 42mm and will wrap around a 30ml bottle.
example of our old label attached.
The design uploaded we are not happy with and would like something a bit more refined. Something that will be memorable and stylish, thinking along the line of up market whiskey or gin labels.
Attached is one of our other labels "ember kissed" and also one of our existing bottles with label.

Thank you, The Bramblecrest Vape Company

PS. Please let us know if you need anything more.
Updates

Project Deadline Extended Reason: Just changed to Guarenteed payment. Just adding a small extension as I am seeing alot of things I do like. Added Tuesday, December 27, 2016

Target Market(s)

18 to 40 year old vapers.

Industry/Entity Type

Industry

Font styles to use
Decorative

Requirements
Must have
• New Logo featured prominently. Barcode integrated (if it can be doned creatively even better)
Nice to have
• Integration of our old "wiener dog"

```html
<!DOCTYPE html>
<html lang="en">
<head>
<meta charset="utf-8">
<title>Bramblecrest Vape Labels</title>
<link href="https://fonts.googleapis.com/css2?family=Fredericka+the+Great&family=Cutive+Mono&display=swap" rel="stylesheet">
<style>
  :root{
    --page:#1b1a18;
    --label:#0d0d0d;
    --silver:#e9e9e9;
    --coral:#ef5b4c;
    --gold:#d9bd5f;
  }
  *{box-sizing:border-box;margin:0;padding:0}
  html,body{width:1200px;height:1200px;overflow:hidden;background:var(--page)}
  .label-row{
    width:1200px;height:1200px;display:flex;align-items:center;justify-content:center;gap:50px;
  }
  .label{
    --ink:var(--silver);
    position:relative;width:340px;height:480px;background:var(--label);
    color:var(--ink);font-family:"Cutive Mono",monospace;
  }
  .label--coral{--ink:var(--coral)}
  .label--gold{--ink:var(--gold)}
  .label__frame{
    position:absolute;inset:14px;border:1px solid var(--ink);opacity:.8;
  }
  .label__mark{
    position:absolute;top:44px;left:0;right:0;display:flex;justify-content:center;
  }
  .label__mark-dot{width:12px;height:12px;border-radius:50%;background:var(--ink)}
  .label__rule{position:absolute;left:34px;right:34px;height:1px;background:var(--ink)}
  .label__rule--top{top:98px}
  .label__rule--bottom{top:128px}
  .label__brand{
    position:absolute;top:105px;left:0;right:0;text-align:center;font-size:14px;letter-spacing:1px;
    white-space:nowrap;
  }
  .label__kicker{
    position:absolute;top:150px;left:0;right:0;text-align:center;
    font-family:"Fredericka the Great",serif;font-size:40px;color:#fff;
  }
  .label__title{
    position:absolute;top:194px;left:0;right:0;text-align:center;
    font-family:"Fredericka the Great",serif;font-size:68px;color:#fff;letter-spacing:1px;
    text-shadow:3px 3px 0 var(--ink);
  }
  .label__side-line{position:absolute;top:300px;width:70px;height:1px;background:var(--ink)}
  .label__side-line--left{left:40px}
  .label__side-line--right{right:40px}
  .label__aged{
    position:absolute;top:284px;left:0;right:0;text-align:center;font-size:19px;line-height:22px;letter-spacing:2px;
  }
  .label__volume{position:absolute;left:34px;top:388px;font-size:20px;letter-spacing:1px}
  .label__hound{
    position:absolute;right:52px;top:350px;width:120px;height:80px;border-radius:40px 40px 10px 30px;
    background:var(--ink);opacity:.85;
  }
</style>
</head>
<body>
<main class="label-row">

  <article class="label label--silver">
    <div class="label__frame"></div>
    <div class="label__mark"><span class="label__mark-dot"></span></div>
    <div class="label__rule label__rule--top"></div>
    <p class="label__brand">BRAMBLECREST VAPE COMPANY</p>
    <div class="label__rule label__rule--bottom"></div>
    <p class="label__kicker">FOX</p>
    <h2 class="label__title">TRAIL</h2>
    <div class="label__side-line label__side-line--left"></div>
    <p class="label__aged">AGED<br>2015</p>
    <div class="label__side-line label__side-line--right"></div>
    <p class="label__volume">10ML</p>
    <div class="label__hound" role="img" aria-label="Engraved illustration of a long-eared dog"></div>
  </article>

  <article class="label label--coral">
    <div class="label__frame"></div>
    <div class="label__mark"><span class="label__mark-dot"></span></div>
    <div class="label__rule label__rule--top"></div>
    <p class="label__brand">BRAMBLECREST VAPE COMPANY</p>
    <div class="label__rule label__rule--bottom"></div>
    <p class="label__kicker">GOOD</p>
    <h2 class="label__title">PUP</h2>
    <div class="label__side-line label__side-line--left"></div>
    <p class="label__aged">AGED<br>2015</p>
    <div class="label__side-line label__side-line--right"></div>
    <p class="label__volume">10ML</p>
    <div class="label__hound" role="img" aria-label="Engraved illustration of a long-eared dog"></div>
  </article>

  <article class="label label--gold">
    <div class="label__frame"></div>
    <div class="label__mark"><span class="label__mark-dot"></span></div>
    <div class="label__rule label__rule--top"></div>
    <p class="label__brand">BRAMBLECREST VAPE COMPANY</p>
    <div class="label__rule label__rule--bottom"></div>
    <p class="label__kicker">MR.</p>
    <h2 class="label__title">SLY</h2>
    <div class="label__side-line label__side-line--left"></div>
    <p class="label__aged">AGED<br>2015</p>
    <div class="label__side-line label__side-line--right"></div>
    <p class="label__volume">10ML</p>
    <div class="label__hound" role="img" aria-label="Engraved illustration of a long-eared dog"></div>
  </article>

</main>
</body>
</html>
```